" Soluçoes de tecnologia focadas em impressao e outsourcing de impressao visando a reduçao de custos de impressao e a melhoria de processos para pequenas, médias e grandes empresas corporativas e governo através de licitações. Atendimento ao público(balcão) com soluções de grafica rápida, impressão de dados variáveis, impressão de provas de consursos Gerenciar e racionalizar os processos de impressao/cópia através de uso inteligente de tecnologia de última geraçao. Contabilizar páginas/cópias impressas, gerenciar suprimentos. Otimizar processos internos para cada departamento e necessidade. Solução de digitalização de documentos. "

```html
<!DOCTYPE html>
<html lang="pt-BR">
<head>
<meta charset="utf-8">
<title>Tonare Outsourcing — Soluções que impressionam</title>
<link rel="stylesheet" href="https://fonts.googleapis.com/css2?family=Roboto+Condensed:wght@400;700;800&family=Roboto:wght@400;500;700&display=swap">
<style>
  :root{
    --page-bg:#e9eaec;
    --brand-red:#e3111b;
    --ink:#1d1d1f;
    --muted:#6b6f76;
    --navy-deep:#0d2a6b;
    --navy:#16409a;
    --navy-light:#2a62c9;
    --sky:#8fc3ff;
    --white:#ffffff;
    --dark-btn:#222428;
  }
  *{box-sizing:border-box;margin:0;padding:0}
  html,body{width:1200px;height:1200px;overflow:hidden}
  body{
    background:var(--page-bg);
    font-family:"Roboto",Arial,sans-serif;
    display:flex;align-items:center;justify-content:center;
  }
  .site{
    width:1200px;height:760px;background:var(--white);
    display:flex;flex-direction:column;
    box-shadow:0 10px 40px rgba(0,0,0,.12);
  }
  .accent-strip{height:6px;background:var(--brand-red)}
  .top-bar{
    height:30px;display:flex;align-items:center;gap:28px;
    padding:0 60px;font-size:12px;color:var(--muted);
    border-bottom:1px solid #eee;
  }
  .top-bar .phone{color:var(--brand-red);font-weight:500}
  .header{
    height:86px;display:flex;align-items:center;justify-content:space-between;
    padding:0 60px;
  }
  .brand{display:flex;align-items:center;gap:10px;
    font-family:"Roboto Condensed",Arial,sans-serif;font-weight:800;
    font-size:34px;color:var(--ink);letter-spacing:-.5px}
  .brand-mark{width:22px;height:22px;background:var(--brand-red)}
  .nav{display:flex;align-items:center;gap:26px;
    font-family:"Roboto Condensed",Arial,sans-serif;font-weight:700;
    font-size:14px;color:var(--ink);text-transform:uppercase}
  .nav .is-active{border:2px solid var(--brand-red);color:var(--brand-red);padding:4px 10px}
  .nav .support-btn{background:var(--dark-btn);color:var(--white);
    padding:9px 20px;border-radius:20px;margin-left:10px}
  .hero{
    position:relative;flex:1;overflow:hidden;
    background:linear-gradient(120deg,var(--navy-deep) 0%,var(--navy) 50%,var(--navy-light) 100%);
  }
  .hero-pattern{position:absolute;inset:0;
    background:radial-gradient(circle at 65% 40%,rgba(90,150,255,.35),transparent 60%)}
  .hero-copy{position:absolute;left:150px;top:160px;width:480px;text-align:center}
  .hero-kicker{font-family:"Roboto Condensed",Arial,sans-serif;font-size:30px;
    color:var(--sky);letter-spacing:.5px;text-transform:uppercase}
  .hero-title{font-family:"Roboto Condensed",Arial,sans-serif;font-weight:800;
    font-size:66px;line-height:1.02;color:var(--white);text-transform:uppercase;margin-top:10px}
  .hero-actions{display:flex;justify-content:center;gap:24px;margin-top:38px}
  .btn{font-family:"Roboto Condensed",Arial,sans-serif;font-size:14px;font-weight:700;
    text-transform:uppercase;padding:11px 26px;border-radius:22px;color:var(--white)}
  .btn-outline{border:2px solid var(--sky)}
  .btn-solid{background:var(--brand-red);border:2px solid var(--brand-red)}
  .hero-product{position:absolute;left:700px;top:60px;width:300px;height:380px;
    background:linear-gradient(180deg,#f2f3f5,#c9ccd2);border-radius:6px}
  .slider-arrow{position:absolute;top:50%;width:34px;height:34px;margin-top:-17px;
    background:var(--white);display:flex;align-items:center;justify-content:center}
  .slider-arrow.prev{left:40px}
  .slider-arrow.next{right:40px}
  .slider-dots{position:absolute;bottom:34px;left:50%;transform:translateX(-50%);display:flex;gap:10px}
  .slider-dots span{width:9px;height:9px;border-radius:50%;background:rgba(255,255,255,.45)}
  .slider-dots span.on{background:var(--white)}
</style>
</head>
<body>
  <div class="site">
    <div class="accent-strip"></div>
    <div class="top-bar">
      <span class="email">contato@tonare.com.br</span>
      <span class="phone">(11) 4000-1234</span>
    </div>
    <header class="header">
      <div class="brand"><span class="brand-mark"></span>Tonare</div>
      <nav class="nav">
        <span class="is-active">Início</span>
        <span>Quem somos</span>
        <span>Soluções</span>
        <span>Portfólio</span>
        <span>Fale conosco</span>
        <span class="support-btn">Suporte online</span>
      </nav>
    </header>
    <section class="hero">
      <div class="hero-pattern" role="img" aria-label="Fundo azul com padrão de quadrados"></div>
      <div class="hero-product" role="img" aria-label="Foto de impressora multifuncional"></div>
      <div class="hero-copy">
        <p class="hero-kicker">Outsourcing de impressão</p>
        <h1 class="hero-title">Soluções que<br>impressionam</h1>
        <div class="hero-actions">
          <span class="btn btn-outline">Saiba mais</span>
          <span class="btn btn-solid">Fale conosco</span>
        </div>
      </div>
      <span class="slider-arrow prev"><svg width="12" height="14" viewBox="0 0 12 14"><path d="M10 1 3 7l7 6" fill="none" stroke="#16409a" stroke-width="3"/></svg></span>
      <span class="slider-arrow next"><svg width="12" height="14" viewBox="0 0 12 14"><path d="m2 1 7 6-7 6" fill="none" stroke="#16409a" stroke-width="3"/></svg></span>
      <div class="slider-dots"><span class="on"></span><span></span></div>
    </section>
  </div>
</body>
</html>
```